Business Card for Start Up Real Estate Company

We need a business card designed for a new real estate company called Lumivane. We plan on improving the experience of real estate transactions for both consumers and agents by using current and evolving technology. We would like to see designs that use our existing logo (attached). Please use a primarily white or light colored background. The final design should communicate technology, sophistication and customer service. Thank you...

Industry/Entity Type

Real Estate

Requirements
Must have
• Primarily white or light colored background
Nice to have
• Isolated A from our logo used as part of the design
Should not have
• Pictures, especially of houses

```html
<!DOCTYPE html>
<html lang="en">
<head>
<meta charset="utf-8">
<title>Lumivane Business Card</title>
<link href="https://fonts.googleapis.com/css2?family=Mulish:ital,wght@0,300;0,400;0,600;0,700;1,400&display=swap" rel="stylesheet">
<style>
  :root {
    --stage: #e9ebee;
    --card-white: #ffffff;
    --brand-blue: #1b7cc0;
    --brand-blue-deep: #0b5c9c;
    --brand-blue-light: #2f97d6;
    --accent-red: #e4364f;
    --ink: #4a4f56;
    --ink-soft: #7a8089;
    --rule: #9fb8cf;
  }
  * { box-sizing: border-box; margin: 0; padding: 0; }
  html, body {
    width: 1200px;
    height: 1024px;
    overflow: hidden;
    background: var(--stage);
    font-family: "Mulish", "Helvetica Neue", Arial, sans-serif;
  }
  .card {
    position: absolute;
    left: 180px;
    width: 840px;
    height: 480px;
    border-radius: 30px;
    overflow: hidden;
    box-shadow: 0 10px 30px rgba(0,0,0,0.18);
  }
  /* Front side */
  .card--front {
    top: 24px;
    background: linear-gradient(160deg, var(--brand-blue-light) 0%, var(--brand-blue) 45%, var(--brand-blue-deep) 100%);
  }
  .card--front .wordmark {
    position: absolute;
    left: 0; right: 0;
    top: 170px;
    text-align: center;
    color: var(--card-white);
    font-weight: 400;
    font-size: 92px;
    letter-spacing: 4px;
  }
  .card--front .website {
    position: absolute;
    left: 0; right: 0;
    top: 310px;
    text-align: center;
    color: var(--card-white);
    font-size: 26px;
    font-weight: 400;
    letter-spacing: 3px;
  }
  /* Back side */
  .card--back {
    top: 520px;
    background: var(--card-white);
  }
  .card--back .wave {
    position: absolute;
    left: 0; top: 0;
    width: 840px;
    height: 480px;
  }
  .card--back .wordmark {
    position: absolute;
    left: 380px;
    top: 56px;
    color: var(--brand-blue);
    font-weight: 400;
    font-size: 72px;
    letter-spacing: 3px;
  }
  .identity {
    position: absolute;
    right: 470px;
    top: 172px;
    text-align: right;
    color: var(--ink);
  }
  .identity .name {
    color: var(--brand-blue);
    font-weight: 700;
    font-size: 32px;
    line-height: 1.15;
  }
  .identity .role {
    font-style: italic;
    font-size: 19px;
    color: var(--ink-soft);
    margin-bottom: 8px;
  }
  .identity .address {
    font-size: 19px;
    line-height: 1.35;
  }
  .divider {
    position: absolute;
    left: 392px;
    top: 176px;
    width: 1.5px;
    height: 150px;
    background: var(--rule);
  }
  .contacts {
    position: absolute;
    left: 414px;
    top: 186px;
    list-style: none;
    color: var(--ink);
    font-size: 20px;
  }
  .contacts li {
    display: flex;
    align-items: center;
    gap: 14px;
    height: 32px;
  }
  .contacts svg { width: 20px; height: 20px; flex: none; }
</style>
</head>
<body>

<section class="card card--front" aria-label="Card front">
  <div class="wordmark">LUMIVANE</div>
  <div class="website">www.lumivane.com</div>
</section>

<section class="card card--back" aria-label="Card back">
  <svg class="wave" viewBox="0 0 840 480" aria-hidden="true">
    <path d="M0 300 C 220 420, 560 440, 840 440 L 840 480 L 0 480 Z" fill="var(--accent-red)"/>
    <path d="M0 318 C 220 432, 560 452, 840 452 L 840 480 L 0 480 Z" fill="var(--brand-blue)"/>
  </svg>

  <div class="wordmark">LUMIVANE</div>

  <div class="identity">
    <p class="name">Daniel Hartley</p>
    <p class="role">President / Owner</p>
    <p class="address">48 Harbor View Lane<br>Westbrook 20417</p>
  </div>

  <div class="divider"></div>

  <ul class="contacts">
    <li>
      <svg viewBox="0 0 20 20" aria-label="Phone"><path d="M5 2 L8 2 L9 6 L7 8 C8 10.5 9.5 12 12 13 L14 11 L18 12 L18 15 C18 16.5 17 17.5 15.5 17.5 C8.5 17 3 11.5 2.5 4.5 C2.5 3 3.5 2 5 2 Z" fill="var(--accent-red)"/></svg>
      <span>+1 555 210 4830</span>
    </li>
    <li>
      <svg viewBox="0 0 20 20" aria-label="Mobile"><rect x="5" y="1.5" width="10" height="17" rx="2" fill="var(--accent-red)"/><rect x="7" y="4" width="6" height="10" fill="#fff"/><circle cx="10" cy="16.2" r="1" fill="#fff"/></svg>
      <span>+1 555 210 4831</span>
    </li>
    <li>
      <svg viewBox="0 0 20 20" aria-label="Fax"><rect x="6" y="2" width="8" height="5" fill="var(--accent-red)"/><rect x="2" y="7" width="16" height="8" rx="1.5" fill="var(--accent-red)"/><rect x="6" y="12" width="8" height="6" fill="#fff" stroke="var(--accent-red)" stroke-width="1.5"/></svg>
      <span>+1 555 318 7702</span>
    </li>
    <li>
      <svg viewBox="0 0 20 20" aria-label="Email"><rect x="2" y="4" width="16" height="12" rx="1" fill="var(--accent-red)"/><path d="M2.5 5 L10 11 L17.5 5" fill="none" stroke="#fff" stroke-width="1.5"/></svg>
      <span>dhartley@lumivane.com</span>
    </li>
  </ul>
</section>

</body>
</html>
```